A Healthy KORV Louisiana- TWAB Conference Poster

LA Carewell is presenting at the TWAB conference. The TWAB is a annual meeting for State, Federal and private sector individuals to provide opportunities for the exchange of ideas related to Carewell systems and heath policy affected by those systems. Louisiana will be presenting on their LaKORV Program . A poster with the information in the PowerPoint is needed. The first slide shows a draft of organization. The wording on slides two and three should be displayed in a visually appealing infographic. The charts should coordinate with the overall design. We would like to see the Louisiana state capital building incorporated.

Font styles to use
Sans Serif

Colors

Designer to choose colors to be used in the design.

Requirements
Must have
• Visually appealing infographics and charts
Nice to have
• Incorporate the capital building, incorporate the LaKORV logo (on first slide)

```html
<!DOCTYPE html>
<html lang="en">
<head>
<meta charset="utf-8">
<title>A Healthy KORV Louisiana</title>
<link href="https://fonts.googleapis.com/css2?family=Lato:wght@400;700;900&display=swap" rel="stylesheet">
<style>
  :root {
    --sky-top: #2c7cc4;
    --sky-mid: #7fb8e4;
    --sky-low: #d4ebf8;
    --lawn: #3f8a2c;
    --lawn-dark: #2d6b22;
    --panel: rgba(255,255,255,0.84);
    --heading-green: #5aa02c;
    --item-blue: #2c6fb5;
    --text-dark: #333a40;
    --table-head: #4a74c4;
    --row-a: #d6dff1;
    --row-b: #eaeef7;
    --white: #ffffff;
    --stone-light: rgba(214,206,186,0.95);
    --stone-dark: rgba(150,140,118,0.95);
  }
  * { box-sizing: border-box; margin: 0; padding: 0; }
  html, body { width: 1200px; height: 633px; overflow: hidden; }
  body { font-family: "Lato", Arial, sans-serif; color: var(--text-dark); }

  .poster {
    position: relative; width: 1200px; height: 633px; overflow: hidden;
    background: linear-gradient(180deg, var(--sky-top) 0%, var(--sky-mid) 45%, var(--sky-low) 78%);
  }
  .scenery-lawn {
    position: absolute; left: 0; right: 0; bottom: 0; height: 92px;
    background: linear-gradient(180deg, #8fbf6a 0%, var(--lawn) 35%, var(--lawn-dark) 100%);
  }
  .capitol-photo {
    position: absolute; left: 505px; top: 66px; width: 190px; height: 480px;
    background:
      linear-gradient(90deg, rgba(255,255,255,0) 0%, rgba(255,255,255,0) 100%),
      linear-gradient(180deg, var(--stone-light) 0%, var(--stone-dark) 100%);
    -webkit-mask-image: radial-gradient(ellipse 50% 55% at 50% 55%, #000 55%, transparent 100%);
    mask-image: radial-gradient(ellipse 50% 55% at 50% 55%, #000 55%, transparent 100%);
  }

  .title {
    position: absolute; left: 29px; top: 44px;
    font-size: 41px; font-weight: 900; color: var(--white); letter-spacing: -0.3px;
  }
  .intro {
    position: absolute; left: 700px; top: 44px; width: 460px;
    color: var(--white); font-size: 9.5px; line-height: 1.35; text-align: center;
  }
  .intro p + p { margin-top: 8px; }

  .panel {
    position: absolute; background: var(--panel);
    display: flex; gap: 10px; padding: 14px 14px 12px;
  }
  .panel--obstacles { left: 26px; top: 144px; width: 482px; height: 243px; }
  .panel--solutions { left: 692px; top: 139px; width: 482px; height: 248px; }
  .panel__text { width: 185px; flex-shrink: 0; }
  .panel__heading {
    font-size: 16px; font-weight: 900; color: var(--heading-green); margin-bottom: 8px;
  }
  .item__title { font-size: 7px; font-weight: 900; color: var(--item-blue); text-transform: uppercase; margin-top: 6px; }
  .item__body { font-size: 6.6px; line-height: 1.35; }
  .panel__chart { flex: 1; }
  .panel__chart svg { width: 100%; height: 100%; }

  .table-panel {
    position: absolute; background: var(--panel); padding: 12px 16px;
  }
  .table-panel--before { left: 26px; top: 423px; width: 482px; height: 122px; }
  .table-panel--after { left: 692px; top: 423px; width: 482px; height: 131px; }
  .cases-table { width: 100%; border-collapse: separate; border-spacing: 0 1px; font-size: 7px; }
  .cases-table th { background: var(--table-head); color: var(--white); text-align: left; padding: 2px 8px; font-weight: 700; }
  .cases-table td { padding: 2.5px 8px; }
  .cases-table tr:nth-child(odd) td { background: var(--row-a); }
  .cases-table tr:nth-child(even) td { background: var(--row-b); }

  .brand {
    position: absolute; left: 471px; top: 518px; width: 258px; height: 258px;
    border-radius: 50%; background: var(--white);
    display: flex; flex-direction: column; align-items: center; padding-top: 20px;
  }
  .brand__tag { font-size: 6.5px; line-height: 1.25; color: var(--text-dark); text-align: center; margin-bottom: 4px; }
  .brand__row { display: flex; align-items: center; gap: 8px; }
  .brand__mark { width: 24px; height: 24px; background: var(--heading-green); }
  .brand__name { font-size: 28px; font-weight: 900; color: var(--item-blue); }
</style>
</head>
<body>
<main class="poster">
  <div class="capitol-photo" role="img" aria-label="Photograph of the Louisiana State Capitol tower"></div>
  <div class="scenery-lawn" role="img" aria-label="Capitol lawn with trees and flowering shrubs"></div>

  <h1 class="title">A Healthy KORV Louisiana</h1>

  <div class="intro">
    <p>Louisiana Coverage Support Payment (LaKORV) program allows for Carewell to pay the premium costs of member's private health insurance when cost effective for the State.</p>
    <p>To increase program participation the State is implementing strategic changes to increase enrollment by 95%, resulting in an $11.2M cost savings to the State by the end of SFY23.</p>
  </div>

  <section class="panel panel--obstacles">
    <div class="panel__text">
      <h2 class="panel__heading">THE OBSTACLES:</h2>
      <h3 class="item__title">Budget Constraints</h3>
      <p class="item__body">Due to a budgetary shortfall the LaKORV program was discontinued on Dec 2015. By ending the program, all members were forced to cover their private insurance premiums, or switch to Carewell.</p>
      <h3 class="item__title">Lack of Public Knowledge</h3>
      <p class="item__body">Members are unaware that this program exists or find it hard to believe that Carewell will pay for their private health insurance.</p>
      <h3 class="item__title">Lack of Participation</h3>
      <p class="item__body">Cost effectiveness formula is too restrictive excluding a large portion of the viable population, including waiver, Fee for Service (FFS) members and the individual insurance market.</p>
      <h3 class="item__title">Crowd Out</h3>
      <p class="item__body">Crowd out occurs when members choose public insurance in lieu of available private health insurance.</p>
    </div>
    <div class="panel__chart">
      <svg viewBox="0 0 300 210" aria-label="LaKORV participation FY12 to FY16">
        <text x="165" y="12" text-anchor="middle" font-size="10" fill="#2a5aa8" font-family="Lato, sans-serif">LaKORV Participation</text>
        <g stroke="#c8ccd2" stroke-width="0.6">
          <line x1="40" y1="20" x2="290" y2="20"/><line x1="40" y1="37.5" x2="290" y2="37.5"/>
          <line x1="40" y1="55" x2="290" y2="55"/><line x1="40" y1="72.5" x2="290" y2="72.5"/>
          <line x1="40" y1="90" x2="290" y2="90"/><line x1="40" y1="107.5" x2="290" y2="107.5"/>
          <line x1="40" y1="125" x2="290" y2="125"/><line x1="40" y1="142.5" x2="290" y2="142.5"/>
          <line x1="40" y1="160" x2="290" y2="160"/>
        </g>
        <g font-size="6" fill="#333a40" text-anchor="end" font-family="Lato, sans-serif">
          <text x="36" y="22">1600</text><text x="36" y="39.5">1400</text><text x="36" y="57">1200</text>
          <text x="36" y="74.5">1000</text><text x="36" y="92">800</text><text x="36" y="109.5">600</text>
          <text x="36" y="127">400</text><text x="36" y="144.5">200</text><text x="36" y="162">0</text>
        </g>
        <g font-size="6" fill="#333a40" text-anchor="middle" font-family="Lato, sans-serif">
          <text x="60" y="172">FY12</text><text x="115" y="172">FY13</text><text x="170" y="172">FY14</text>
          <text x="225" y="172">FY15</text><text x="280" y="172">FY16</text>
          <text x="165" y="186" font-weight="700">Fiscal Year</text>
          <text transform="translate(12 90) rotate(-90)" font-weight="700">Number of LaKORV Cases</text>
        </g>
        <polyline points="60,160 115,116.25 170,72.5 225,28.75 280,160" fill="none" stroke="#2a5aa8" stroke-width="1.6"/>
      </svg>
    </div>
  </section>

  <section class="panel panel--solutions">
    <div class="panel__text">
      <h2 class="panel__heading">THE SOLUTIONS:</h2>
      <h3 class="item__title">Program Restored</h3>
      <p class="item__body">LaKORV was reinstated in April 2017, restoring LCH's focus on promoting employer-sponsored insurance.</p>
      <h3 class="item__title">Increase Awareness and Public Knowledge</h3>
      <p class="item__body">LCH has contracted a marketing firm to develop a comprehensive marketing and outreach strategy aimed at engaging providers, employers, insurance companies and members.</p>
      <h3 class="item__title">Increase Participation</h3>
      <p class="item__body">Refinement of the cost effectiveness formula increased the pool of members eligible for the program, including waiver, Fee for Service (FFS) members and the individual insurance market.</p>
      <h3 class="item__title">Data and Analytics</h3>
      <p class="item__body">The use of data mining identifies individuals and populations to be targeted for program outreach.</p>
    </div>
    <div class="panel__chart">
      <svg viewBox="0 0 300 210" aria-label="LaKORV participation FY17 to FY23">
        <text x="165" y="12" text-anchor="middle" font-size="10" fill="#2a5aa8" font-family="Lato, sans-serif">LaKORV Participation</text>
        <g stroke="#c8ccd2" stroke-width="0.6">
          <line x1="40" y1="20" x2="290" y2="20"/><line x1="40" y1="37.5" x2="290" y2="37.5"/>
          <line x1="40" y1="55" x2="290" y2="55"/><line x1="40" y1="72.5" x2="290" y2="72.5"/>
          <line x1="40" y1="90" x2="290" y2="90"/><line x1="40" y1="107.5" x2="290" y2="107.5"/>
          <line x1="40" y1="125" x2="290" y2="125"/><line x1="40" y1="142.5" x2="290" y2="142.5"/>
          <line x1="40" y1="160" x2="290" y2="160"/>
        </g>
        <g font-size="6" fill="#333a40" text-anchor="end" font-family="Lato, sans-serif">
          <text x="36" y="22">1600</text><text x="36" y="39.5">1400</text><text x="36" y="57">1200</text>
          <text x="36" y="74.5">1000</text><text x="36" y="92">800</text><text x="36" y="109.5">600</text>
          <text x="36" y="127">400</text><text x="36" y="144.5">200</text><text x="36" y="162">0</text>
        </g>
        <g font-size="6" fill="#333a40" text-anchor="middle" font-family="Lato, sans-serif">
          <text x="60" y="172">FY17</text><text x="104" y="172">FY19</text><text x="148" y="172">FY20</text>
          <text x="192" y="172">FY21</text><text x="236" y="172">FY22</text><text x="280" y="172">FY23</text>
          <text x="165" y="186" font-weight="700">Fiscal Year</text>
          <text transform="translate(12 90) rotate(-90)" font-weight="700">Number of LaKORV Cases</text>
        </g>
        <polyline points="60,160 104,121.9 148,110.5 192,86 236,63.5 280,34.5" fill="none" stroke="#2a5aa8" stroke-width="1.6"/>
        <g fill="#2a5aa8">
          <circle cx="60" cy="160" r="2"/><circle cx="104" cy="121.9" r="2"/><circle cx="148" cy="110.5" r="2"/>
          <circle cx="192" cy="86" r="2"/><circle cx="236" cy="63.5" r="2"/><circle cx="280" cy="34.5" r="2"/>
        </g>
        <g font-size="5" fill="#333a40" text-anchor="middle" font-family="Lato, sans-serif">
          <text x="60" y="146">Program</text><text x="60" y="152">Restored</text>
          <text x="100" y="112">Current</text>
          <text x="134" y="92">Marketing Firm</text><text x="134" y="98">Engaged</text>
          <text x="174" y="116">Formula</text><text x="174" y="122">Refined</text>
        </g>
      </svg>
    </div>
  </section>

  <section class="table-panel table-panel--before">
    <table class="cases-table">
      <thead><tr><th>Fiscal Year</th><th>Number of LaKORV Cases</th><th>Key Events</th></tr></thead>
      <tbody>
        <tr><td>FY12</td><td>0</td><td></td></tr>
        <tr><td>FY13</td><td>500</td><td></td></tr>
        <tr><td>FY14</td><td>1000</td><td></td></tr>
        <tr><td>FY15</td><td>1500</td><td>Funding Lost</td></tr>
        <tr><td>FY16</td><td>0</td><td></td></tr>
      </tbody>
    </table>
  </section>

  <section class="table-panel table-panel--after">
    <table class="cases-table">
      <thead><tr><th>Fiscal Year</th><th>Number of LaKORV Cases</th><th>Key Events</th></tr></thead>
      <tbody>
        <tr><td>FY17</td><td>0</td><td>Program Restored</td></tr>
        <tr><td>FY19</td><td>435</td><td>Current</td></tr>
        <tr><td>FY20</td><td>566</td><td>Marketing Firm Engaged<br>Formula Refined</td></tr>
        <tr><td>FY21</td><td>846</td><td></td></tr>
        <tr><td>FY22</td><td>1,103</td><td></td></tr>
        <tr><td>FY23</td><td>1,434</td><td></td></tr>
      </tbody>
    </table>
  </section>

  <div class="brand">
    <p class="brand__tag">The Louisiana Coverage Support<br>Payment Program</p>
    <div class="brand__row">
      <span class="brand__mark"></span>
      <span class="brand__name">LaKORV</span>
    </div>
  </div>
</main>
</body>
</html>
```